Ridgeway Builders, Inc. Concrete cutting special flyer , 10% off for new customers

Flyer to send to potential customers and business associates and general contractors - specializing in Concrete-Flatwork
Concrete Repair
Concrete Sidewalks
Patios & Driveways
Stoops, Porches And Staircase
Foundation Contractors--Concrete
Facade Restoration
Concrete
Patios
Driveways
Walkways
Commercial Concrete Work
Concrete Restoration
Building Alterations
Foundations - Concrete
Concrete Repairs
rbwxpo.com

Target Market(s)

Homeowners, business owners & general contractors

Industry/Entity Type

Construction

Font styles to use
Serif

Colors
FFC000
F8CF3A
FAE287
FDF2CF
FEFAEE
EB3D1F
EC4F4E
F09395
F8D3D4
FCEDEE

Requirements
Must have
• General Contracting, masonry - Must have Logo Please see list of services Ridgeway Builders NY, Inc., has to offer. Concrete-Flatwork Concrete Repair Concrete Sidewalks Patios & Driveways Stoops, Porches And Staircase Foundation Contractors--Concrete Facade Restoration Concrete Patios Driveways Walkways Commercial Concrete Work Concrete Restoration Building Alterations Foundations - Concrete Concrete Repairs
Nice to have
• List of services - Logo - Black & Gold with a bold color to stand out (preferably reds)

```html
<!DOCTYPE html>
<html lang="en">
<head>
<meta charset="utf-8">
<title>Ridgeway Builders – Build &amp; Renovate</title>
<link href="https://fonts.googleapis.com/css2?family=Oswald:wght@500;700&family=Open+Sans:wght@400;600;700&display=swap" rel="stylesheet">
<style>
:root{
  --gold:#FFC000;
  --gold-soft:#F8CF3A;
  --ink:#1e1e1e;
  --panel:#262626;
  --white:#ffffff;
  --muted:#d9d9d9;
  --red:#EB3D1F;
}
*{margin:0;padding:0;box-sizing:border-box}
html,body{width:861px;height:1200px;overflow:hidden;background:#fff}
.flyer{position:relative;width:861px;height:1200px;font-family:"Open Sans",sans-serif;overflow:hidden;background:var(--white)}
.brand{position:absolute;left:0;top:0;width:272px;height:245px;display:flex;flex-direction:column;align-items:center;justify-content:center;gap:12px}
.brand-mark{width:34px;height:34px;background:var(--gold)}
.brand-name{font-family:"Oswald",sans-serif;font-weight:700;font-size:26px;color:var(--ink);text-align:center;line-height:1.15;text-transform:uppercase}
.intro{position:absolute;left:0;top:245px;width:272px;height:675px;background:var(--gold);padding:26px 22px 0 26px}
.intro h2{font-family:"Oswald",sans-serif;font-weight:700;font-size:38px;line-height:1.05;color:var(--ink);text-transform:uppercase}
.intro p{font-size:12.5px;line-height:1.45;color:var(--ink);margin:14px 0 14px}
.services{list-style:none}
.services li{display:flex;align-items:center;gap:8px;font-size:14px;line-height:26px;color:var(--ink)}
.services svg{flex:none}
.photo{position:absolute;left:0;width:272px}
.photo-worker{top:920px;height:140px;background:linear-gradient(160deg,#b9d3e6,#6e8aa0 60%,#c9a23a)}
.photo-excavator{top:1060px;height:140px;background:linear-gradient(180deg,#f0b36a,#c7722f 55%,#3a3028)}
.panel{position:absolute;left:272px;top:0;width:589px;height:1105px;background:var(--panel)}
.site-photo{position:absolute;left:300px;top:600px;width:289px;height:505px;background:linear-gradient(180deg,#3b3b3b,#1c1c1c 70%,#2b2b2b)}
.headline{position:absolute;left:0;right:0;top:24px;text-align:center;font-family:"Oswald",sans-serif;font-weight:700;font-size:60px;line-height:1;color:var(--gold);text-transform:uppercase}
.tagline{position:absolute;left:0;right:0;top:168px;text-align:center;font-family:"Oswald",sans-serif;font-weight:700;font-size:34px;color:var(--white);text-transform:uppercase;letter-spacing:.5px}
.about{position:absolute;left:90px;right:40px;top:228px;font-size:11.5px;line-height:1.5;color:var(--muted);text-align:left}
.hero-machine{position:absolute;left:90px;top:300px;width:440px;height:320px;border-radius:6px;background:radial-gradient(ellipse at 50% 55%,#e0b420 0%,#8a7a3a 40%,#262626 72%)}
.services-title{position:absolute;left:32px;top:640px;font-family:"Oswald",sans-serif;font-weight:700;line-height:1.05;text-transform:uppercase}
.services-title .small{display:block;font-size:30px;color:var(--gold)}
.services-title .big{display:block;font-size:40px;color:var(--white)}
.services-copy{position:absolute;left:32px;width:300px;top:745px;font-size:12.5px;line-height:1.5;color:var(--muted)}
.offer{position:absolute;left:373px;top:912px;width:115px;height:93px;background:var(--gold);text-align:center;padding-top:10px;font-family:"Oswald",sans-serif;color:var(--ink)}
.offer .pct{display:block;font-size:32px;font-weight:700;line-height:1}
.offer .note{display:block;margin-top:10px;background:var(--white);font-family:"Open Sans",sans-serif;font-size:11px;font-weight:600;padding:3px 0;margin-left:8px;margin-right:8px}
.closing{position:absolute;left:32px;top:1032px;font-family:"Oswald",sans-serif;font-weight:700;font-size:21px;line-height:1.35;text-transform:uppercase}
.closing .line1{display:block;color:var(--white)}
.closing .line2{display:block;color:var(--gold)}
.footer{position:absolute;left:272px;top:1105px;width:589px;height:95px;background:var(--white);display:flex;align-items:center;padding:0 24px;gap:20px}
.footer-brand{display:flex;flex-direction:column;align-items:center;gap:4px;width:150px}
.footer-brand .mark{width:16px;height:16px;background:var(--gold)}
.footer-brand .name{font-family:"Oswald",sans-serif;font-weight:700;font-size:13px;color:var(--ink);text-align:center}
.contact{display:flex;align-items:center;gap:10px;font-size:13px;font-weight:600;color:var(--ink)}
.icon-box{width:32px;height:32px;background:var(--gold);display:flex;align-items:center;justify-content:center;flex:none}
.phones{line-height:1.5}
</style>
</head>
<body>
<div class="flyer">
  <div class="brand">
    <span class="brand-mark"></span>
    <span class="brand-name">Ridgeway Builders<br>NY, Inc.</span>
  </div>

  <section class="intro">
    <h2>We Build<br>Your Dream</h2>
    <p>We offer an end-to-end client experience that includes seamless communication, budgeting, staffing, on-site organization, and solid, quality handiwork every time.</p>
    <ul class="services">
      <li><svg width="13" height="13" viewBox="0 0 13 13"><path d="M1 7l4 4 7-9" fill="none" stroke="#1e1e1e" stroke-width="2"/></svg>Concrete Flatwork</li>
      <li><svg width="13" height="13" viewBox="0 0 13 13"><path d="M1 7l4 4 7-9" fill="none" stroke="#1e1e1e" stroke-width="2"/></svg>Concrete Repair</li>
      <li><svg width="13" height="13" viewBox="0 0 13 13"><path d="M1 7l4 4 7-9" fill="none" stroke="#1e1e1e" stroke-width="2"/></svg>Concrete Sidewalks</li>
      <li><svg width="13" height="13" viewBox="0 0 13 13"><path d="M1 7l4 4 7-9" fill="none" stroke="#1e1e1e" stroke-width="2"/></svg>Patios &amp; Driveways</li>
      <li><svg width="13" height="13" viewBox="0 0 13 13"><path d="M1 7l4 4 7-9" fill="none" stroke="#1e1e1e" stroke-width="2"/></svg>Stoops, Porches And Staircase</li>
      <li><svg width="13" height="13" viewBox="0 0 13 13"><path d="M1 7l4 4 7-9" fill="none" stroke="#1e1e1e" stroke-width="2"/></svg>Foundation Contractors–Concrete</li>
      <li><svg width="13" height="13" viewBox="0 0 13 13"><path d="M1 7l4 4 7-9" fill="none" stroke="#1e1e1e" stroke-width="2"/></svg>Facade Restoration</li>
      <li><svg width="13" height="13" viewBox="0 0 13 13"><path d="M1 7l4 4 7-9" fill="none" stroke="#1e1e1e" stroke-width="2"/></svg>Concrete</li>
      <li><svg width="13" height="13" viewBox="0 0 13 13"><path d="M1 7l4 4 7-9" fill="none" stroke="#1e1e1e" stroke-width="2"/></svg>Patios</li>
      <li><svg width="13" height="13" viewBox="0 0 13 13"><path d="M1 7l4 4 7-9" fill="none" stroke="#1e1e1e" stroke-width="2"/></svg>Driveways</li>
      <li><svg width="13" height="13" viewBox="0 0 13 13"><path d="M1 7l4 4 7-9" fill="none" stroke="#1e1e1e" stroke-width="2"/></svg>Walkways</li>
      <li><svg width="13" height="13" viewBox="0 0 13 13"><path d="M1 7l4 4 7-9" fill="none" stroke="#1e1e1e" stroke-width="2"/></svg>Commercial Concrete Work</li>
      <li><svg width="13" height="13" viewBox="0 0 13 13"><path d="M1 7l4 4 7-9" fill="none" stroke="#1e1e1e" stroke-width="2"/></svg>Concrete Restoration</li>
      <li><svg width="13" height="13" viewBox="0 0 13 13"><path d="M1 7l4 4 7-9" fill="none" stroke="#1e1e1e" stroke-width="2"/></svg>Building Alterations</li>
      <li><svg width="13" height="13" viewBox="0 0 13 13"><path d="M1 7l4 4 7-9" fill="none" stroke="#1e1e1e" stroke-width="2"/></svg>Foundations - Concrete</li>
      <li><svg width="13" height="13" viewBox="0 0 13 13"><path d="M1 7l4 4 7-9" fill="none" stroke="#1e1e1e" stroke-width="2"/></svg>Concrete Repairs</li>
    </ul>
  </section>

  <div class="photo photo-worker" role="img" aria-label="Construction worker in hard hat and safety vest on site"></div>
  <div class="photo photo-excavator" role="img" aria-label="Excavator working at sunset"></div>

  <section class="panel">
    <div class="site-photo" role="img" aria-label="Dark construction site with building frame and crane"></div>
    <h1 class="headline">Build &amp;<br>Renovate</h1>
    <div class="tagline">Over 20 Years Experience</div>
    <p class="about">Our projects include both Residential and Commercial construction and repairs/restorations. Occupied and fully operational job sites are never a problem. And we can also plan, manage, and build multi-phase jobs. We specialize in excavation, foundation, roofing and waterproofing.</p>
    <div class="hero-machine" role="img" aria-label="Yellow and black compact excavator"></div>
    <h2 class="services-title"><span class="small">We Provide</span><span class="big">The Best Services</span></h2>
    <p class="services-copy">We work with architects and designers to produce beautiful, functional structures. Call us today and bring our project management skills and extensive construction experience to your next project.</p>
    <div class="offer"><span class="pct">10%</span><span class="pct" style="font-size:20px">off</span><span class="note">for new customers</span></div>
    <p class="closing"><span class="line1">We have completed lot of projects.</span><span class="line2">You can hire us for your future project.</span></p>
  </section>

  <footer class="footer">
    <div class="footer-brand"><span class="mark"></span><span class="name">Ridgeway Builders NY, Inc.</span></div>
    <div class="contact">
      <span class="icon-box"><svg width="16" height="16" viewBox="0 0 16 16"><circle cx="8" cy="8" r="6.5" fill="none" stroke="#1e1e1e" stroke-width="1.5"/><path d="M1.5 8h13M8 1.5c-3 3-3 10 0 13M8 1.5c3 3 3 10 0 13" fill="none" stroke="#1e1e1e" stroke-width="1.2"/></svg></span>
      rbwxpo.com
    </div>
    <div class="contact">
      <span class="icon-box"><svg width="16" height="16" viewBox="0 0 16 16"><path d="M3 1.5l3 3-1.5 2c1 2 2.5 3.5 4.5 4.5l2-1.5 3 3-2 2C7 14 2 9 1.5 3.5z" fill="#1e1e1e"/></svg></span>
      <span class="phones">516-555-0142<br>516-555-0178</span>
    </div>
  </footer>
</div>
</body>
</html>
```